I need a great, modern, professional website for my paint contracting company, Ashbrook Coating Contractors, LLC. I have many good pix that can be used from jobs completed that would be attractive. We do commercial, residential and industrial jobs. I’m fully insured and licensed, including holding a General Contractor’s License as a Subcontractor. I know nothing about coding websites. I’ll have my assistant get on tomorrow and learn how to drop files. I’m not sure what files to send. This will be difficult at best, it being able to talk this through. Oh well. What’s next?

Target Market(s)

General Contractors

Industry/Entity Type

Paint Contracting

Coding

Coded - Design and coding required

Font styles to use
Sans Serif

Colors
00AB8E
00BBA5
67D7C9
C6EFE9
E9F9F6

Requirements
Must have
• Pix of completed jobs, bio, maybe testimonials from happy customers? ….
Nice to have
• I’d like it to have a modern appeal, but still have some warmth.
Should not have
• ??

```html
<!DOCTYPE html>
<html lang="en">
<head>
<meta charset="utf-8">
<title>Ashbrook Coating Contractors, LLC</title>
<link href="https://fonts.googleapis.com/css2?family=Ubuntu:wght@400;500;700&family=Lato:wght@400;700&display=swap" rel="stylesheet">
<style>
:root{
  --green:#00AB8E;
  --green-2:#00BBA5;
  --green-3:#67D7C9;
  --mint:#C6EFE9;
  --mint-2:#E9F9F6;
  --ink:#4a4a4a;
  --dark:#2a2a2a;
  --plum:#3b2a5a;
  --body:#555;
}
*{box-sizing:border-box;margin:0;padding:0}
html,body{width:1200px;height:3372px;overflow:hidden;background:#fff}
body{position:relative;font-family:'Lato',sans-serif;color:var(--body)}
.abs{position:absolute}
a{color:inherit;text-decoration:none}

/* header */
.brand{left:112px;top:24px;font-family:'Ubuntu',sans-serif;font-weight:500;font-size:25px;line-height:30px}
.brand .l1{color:var(--green)}
.brand .l2{color:#6f6f6f}
.nav{display:flex;font-size:17px;color:#333}
.top-nav{left:407px;top:40px;gap:0}
.top-nav a{position:absolute;white-space:nowrap}
.btn{display:flex;align-items:center;justify-content:center;border-radius:30px;font-size:17px;color:#fff}
.btn-call{left:958px;top:31px;width:130px;height:44px;background:var(--green)}

/* hero */
.hero-band{left:70px;top:101px;width:1130px;height:488px;background:linear-gradient(90deg,var(--green-3),var(--green));border-bottom-left-radius:110px}
.hero-photo{left:0;top:101px;width:1200px;height:471px;border-radius:0 0 100px 90px;background:linear-gradient(110deg,#c9ccd0 0%,#8d969c 45%,#56646d 75%,#3d4a52 100%)}
.hero-text{left:677px;top:258px;color:#fff;font-family:'Ubuntu',sans-serif}
.hero-text .welcome{font-size:31px;font-weight:400;line-height:40px}
.hero-text h1{font-size:50px;font-weight:700;line-height:60px;margin-top:6px}

/* section titles */
.title{left:0;width:1200px;text-align:center;font-family:'Ubuntu',sans-serif;font-size:50px;line-height:60px;color:var(--ink);font-weight:700}
.title span{color:var(--green);font-weight:500}

/* services */
.service{top:776px;width:309px;height:292px;overflow:hidden;border-radius:0 150px 150px 150px / 0 146px 146px 146px;color:#fff;text-align:center}
.service .label{position:absolute;left:0;right:0;bottom:38px;font-family:'Ubuntu',sans-serif;font-size:22px;line-height:29px}
.svc-1{left:111px;background:linear-gradient(160deg,#d9b169 0%,#a8926a 40%,#4a4a4a 100%)}
.svc-2{left:446px;background:linear-gradient(160deg,#9aa3aa 0%,#6a737a 50%,#3f4347 100%)}
.svc-3{left:780px;border-radius:150px 24px 150px 150px / 146px 24px 146px 146px;background:linear-gradient(140deg,var(--green-2),var(--green))}
.svc-3 h3{margin-top:72px;font-family:'Ubuntu',sans-serif;font-weight:400;font-size:22px}
.svc-3 p{margin:22px auto 0;width:220px;font-size:14px;line-height:28px}

/* about */
.about{left:0;top:1169px;width:1200px;height:543px;background:var(--green)}
.about h2{position:absolute;left:111px;top:88px;font-family:'Ubuntu',sans-serif;font-size:50px;color:#fff;font-weight:700}
.about p{position:absolute;left:111px;width:490px;font-size:17px;line-height:30px;color:#fff;text-align:justify}
.about .p1{top:172px}
.about .p2{top:310px}
.btn-dark{position:absolute;left:111px;top:413px;width:131px;height:43px;background:#2b2b2b}
.about-ring{left:704px;top:1266px;width:360px;height:360px;border:2px solid #1f3a35;border-radius:50%}
.about-photo{left:734px;top:1263px;width:354px;height:354px;border-radius:50%;background:radial-gradient(circle at 35% 45%,#f1d23b 0%,#e9cd52 30%,#d9dadb 55%,#9aa2ad 80%,#4a6a9a 100%)}

/* gallery */
.shot{}
.g1{left:111px;top:1899px;width:339px;height:217px;border-top-left-radius:22px;background:linear-gradient(180deg,#b9c8d8,#c8a38e 55%,#6d6460)}
.g2{left:468px;top:1899px;width:339px;height:217px;background:linear-gradient(120deg,#e9e7e2 0%,#d6d2cb 45%,#2f5a4e 55%,#26473f 100%)}
.g3{left:827px;top:1899px;width:261px;height:455px;border-top-right-radius:14px;background:linear-gradient(180deg,#1f5fb4 0%,#d8cfbd 40%,#6f6a5f 65%,#5c8a3a 100%)}
.g4{left:111px;top:2137px;width:339px;height:217px;border-bottom-left-radius:22px;background:linear-gradient(110deg,#1b6670 0%,#24707a 55%,#e8eaea 100%)}
.g5{left:468px;top:2137px;width:339px;height:217px;background:linear-gradient(90deg,#2e3b6a,#b9456a 35%,#e8c9b0 55%,#3f7d5e 75%,#d08aa0 100%)}

/* testimonials */
.card{top:2607px;width:459px;height:296px;background:#fff;border-radius:30px;box-shadow:0 4px 30px rgba(0,0,0,.09)}
.card-1{left:114px}
.card-2{left:629px}
.avatar{width:102px;height:102px;border-radius:50%}
.av-1{left:151px;top:2552px;background:radial-gradient(circle,#e98a4c 0%,#3fb6b2 70%)}
.av-2{left:666px;top:2552px;background:radial-gradient(circle,#c8967a 0%,#e3d3e2 70%)}
.card .name{position:absolute;left:37px;top:65px;font-size:21px;color:var(--plum);font-weight:400}
.card .date{position:absolute;left:37px;top:100px;font-size:13px;color:#999}
.card .stars{position:absolute;left:307px;top:69px;display:flex;gap:4px}
.card .quote{position:absolute;left:37px;top:134px;width:374px;font-size:17px;line-height:28px;color:#555;text-align:justify}
.heart{color:#e0202a;font-size:15px}

/* footer */
.foot-band{left:0;top:2980px;width:1200px;height:60px;background:linear-gradient(90deg,var(--green-3),var(--green));border-radius:80px 80px 0 0}
.footer{left:0;top:2997px;width:1200px;height:375px;background:var(--dark);border-radius:90px 90px 0 0;color:#fff}
.foot-brand{position:absolute;left:113px;top:62px;font-family:'Ubuntu',sans-serif;font-size:31px;font-weight:500;line-height:36px}
.foot-nav a{position:absolute;top:81px;font-size:17px;white-space:nowrap}
.rule{position:absolute;left:113px;width:977px;height:1px;background:#4a4a4a}
.info{position:absolute;top:207px;display:flex;gap:12px}
.info h4{font-size:17px;font-weight:700;letter-spacing:.2px}
.info p{font-size:15px;line-height:26px;margin-top:3px}
.copy{position:absolute;left:0;width:1200px;top:339px;text-align:center;font-size:16px}
</style>
</head>
<body>

<header>
  <div class="abs brand"><div class="l1">Ashbrook Coating</div><div class="l2">Contractors, LLC</div></div>
  <nav class="abs top-nav nav">
    <a style="left:0">Home</a><a style="left:75px">About</a><a style="left:152px">Services</a><a style="left:243px">Testimonials</a><a style="left:366px">Gallery</a><a style="left:451px">Contact</a>
  </nav>
  <a class="abs btn btn-call">Get a Call</a>
</header>

<section>
  <div class="abs hero-band"></div>
  <div class="abs hero-photo" role="img" aria-label="Painters on a red boom lift working on a commercial building facade"></div>
  <div class="abs hero-text">
    <div class="welcome">Welcome to</div>
    <h1>Ashbrook Coating<br>Contractors</h1>
  </div>
</section>

<h2 class="abs title" style="top:654px">Our <span>Services</span></h2>
<div class="abs service svc-1" role="img" aria-label="Commercial painting job on an office building"><div class="label">Commercial<br>Painting</div></div>
<div class="abs service svc-2" role="img" aria-label="Painter rolling a residential exterior wall"><div class="label">Residential<br>Painting</div></div>
<div class="abs service svc-3">
  <h3>Industrial Jobs</h3>
  <p>Lorem ipsum dolor sit amet, consectetur adipiscing elit, sed do eius tempor incididunt</p>
</div>

<section class="abs about">
  <h2>About Us</h2>
  <p class="p1">Lorem ipsum dolor sit amet, consectetur adipiscing elit, sed do eiusmod tempor incididunt ut labore et dolore magna aliqua. Quis ipsum suspendisse ultrices gravida. Risus commodo viverra maecenas accumsan lacus vel facilisis.</p>
  <p class="p2">Labore et dolore magna aliqua. Quis ipsum suspendisse ultrices gravida. Risus commodo viverra maecenas accumsan lacus vel.</p>
  <a class="btn btn-dark">Get a Call</a>
</section>
<div class="abs about-ring"></div>
<div class="abs about-photo" role="img" aria-label="Painter in a hard hat rolling yellow paint on a wall"></div>

<h2 class="abs title" style="top:1792px">Our <span>Work</span></h2>
<div class="abs g1" role="img" aria-label="Painted retail plaza exterior"></div>
<div class="abs g2" role="img" aria-label="Living room with dark green accent wall"></div>
<div class="abs g3" role="img" aria-label="Freshly painted two-storey family home"></div>
<div class="abs g4" role="img" aria-label="Teal painted interior with armchair"></div>
<div class="abs g5" role="img" aria-label="Row of colourfully painted storefronts"></div>

<h2 class="abs title" style="top:2443px">Happy <span>Clients</span></h2>
<div class="abs card card-1">
  <div class="name">Dana Whitlow</div>
  <div class="stars"><svg width="120" height="16" viewBox="0 0 120 16"><g fill="#f2c01e"><path id="st" d="M8 0l2.4 5 5.4.6-4 3.7 1.1 5.4L8 12 3.1 14.7 4.2 9.3 .2 5.6 5.6 5z"/><use href="#st" x="26"/><use href="#st" x="52"/><use href="#st" x="78"/><use href="#st" x="104"/></g></svg></div>
  <div class="date">April 13</div>
  <p class="quote">Et harum quidem rerum facilis est et expeddistinctio. Nam libero tempore, cum soluta nobis eligendi optio cumque nihil impedit quo minus id quod maxime placeat, omnis voluptas assumenda est, omnis dolor repellendus. <span class="heart">♥♥</span></p>
</div>
<div class="abs avatar av-1" role="img" aria-label="Client portrait"></div>
<div class="abs card card-2">
  <div class="name">Dana Whitlow</div>
  <div class="stars"><svg width="120" height="16" viewBox="0 0 120 16"><g fill="#f2c01e"><use href="#st"/><use href="#st" x="26"/><use href="#st" x="52"/><use href="#st" x="78"/><use href="#st" x="104"/></g></svg></div>
  <div class="date">April 13</div>
  <p class="quote">Et harum quidem rerum facilis est et expeddistinctio. Nam libero tempore, cum soluta nobis eligendi optio cumque nihil impedit quo minus id quod maxime placeat, omnis voluptas assumenda est, omnis dolor repellendus. <span class="heart">♥♥</span></p>
</div>
<div class="abs avatar av-2" role="img" aria-label="Client portrait"></div>

<div class="abs foot-band"></div>
<footer class="abs footer">
  <div class="foot-brand">Ashbrook Coating<br>Contractors, LLC</div>
  <nav class="foot-nav">
    <a style="left:578px">Home</a><a style="left:653px">About</a><a style="left:729px">Services</a><a style="left:822px">Testimonials</a><a style="left:945px">Gallery</a><a style="left:1030px">Contact</a>
  </nav>
  <div class="rule" style="top:167px"></div>
  <div class="info" style="left:113px">
    <svg width="24" height="26" viewBox="0 0 24 26" fill="none" stroke="#fff" stroke-width="1.8"><path d="M12 24s8-8 8-14a8 8 0 0 0-16 0c0 6 8 14 8 14z"/><circle cx="12" cy="10" r="3"/></svg>
    <div><h4>ADDRESS</h4><p>Ashbrook Coating Contractors,<br>Address Comes Here.</p></div>
  </div>
  <div class="info" style="left:386px">
    <svg width="26" height="22" viewBox="0 0 26 22" fill="none" stroke="#fff" stroke-width="1.8"><rect x="2" y="3" width="22" height="16" rx="2"/><path d="M2 4l11 9 11-9"/></svg>
    <div><h4>EMAIL</h4><p>info@ashbrookcoating.com</p></div>
  </div>
  <div class="info" style="left:684px">
    <svg width="24" height="24" viewBox="0 0 24 24" fill="none" stroke="#fff" stroke-width="1.8"><path d="M5 2h4l2 5-3 2a12 12 0 0 0 7 7l2-3 5 2v4a2 2 0 0 1-2 2A19 19 0 0 1 3 4a2 2 0 0 1 2-2z"/></svg>
    <div><h4>PHONE</h4><p>+1 555-014-2290</p></div>
  </div>
  <div class="info" style="left:896px">
    <svg width="24" height="24" viewBox="0 0 24 24" fill="none" stroke="#fff" stroke-width="2.2"><circle cx="12" cy="12" r="9"/><path d="M12 7v5h-4"/></svg>
    <div><h4>HOURS</h4><p>Mon - Fri 8:30am - 9pm<br>Sat - Sun Closed</p></div>
  </div>
  <div class="rule" style="top:314px"></div>
  <div class="copy">2022 Ashbrook Coating Contractors,LLC. All Rights Reserved.</div>
</footer>

</body>
</html>
```